ashby paving works

Needs to have phone number 0412885107 and email marklowry@pavemail.com.au.
ABN 27613048852
name mark lowry

For all your concreting solutions
Excavation
Exposed & colour concrete
House & shed slabs
Driveways
Landing & steps

Contact Information for Business Card

ph 0412885107
email marklowry@pavemail.com.au.
ABN 27613048852
name mark lowry

```html
<!DOCTYPE html>
<html lang="en">
<head>
<meta charset="utf-8">
<title>Ashby Paving Works — Business Card</title>
<link rel="stylesheet" href="https://fonts.googleapis.com/css2?family=Montserrat:wght@600&family=Arimo:wght@400&display=swap">
<style>
  :root {
    --backdrop: #e4e4e4;
    --card-white: #ffffff;
    --slate: #666565;
    --orange: #ee6a1f;
    --ink: #2b2b2b;
    --muted: #5c5c5c;
  }
  * { margin: 0; padding: 0; box-sizing: border-box; }
  html, body {
    width: 1200px;
    height: 900px;
    overflow: hidden;
    background: var(--backdrop);
  }
  .canvas {
    position: relative;
    width: 1200px;
    height: 900px;
  }
  .card {
    position: absolute;
    left: 250px;
    width: 700px;
    height: 400px;
    overflow: hidden;
    box-shadow: 0 4px 14px rgba(0,0,0,0.12);
  }
  /* Front */
  .card-front { top: 35px; background: var(--orange); }
  .front-band {
    position: absolute;
    left: 0; top: 0;
    width: 100%; height: 170px;
    background: var(--slate);
  }
  .front-square {
    position: absolute;
    left: 300px; top: 120px;
    width: 100px; height: 100px;
    background: var(--slate);
    transform: rotate(45deg);
  }
  .front-name {
    position: absolute;
    left: 0; top: 262px;
    width: 100%;
    text-align: center;
    font-family: "Montserrat", sans-serif;
    font-weight: 600;
    font-size: 34px;
    letter-spacing: 0.5px;
    color: var(--card-white);
    text-transform: uppercase;
  }
  /* Back */
  .card-back { top: 465px; background: var(--card-white); }
  .back-block {
    position: absolute;
    left: 70px; top: 0;
    width: 170px; height: 150px;
    background: var(--slate);
  }
  .back-details {
    position: absolute;
    left: 290px; top: 40px;
    font-family: "Arimo", sans-serif;
    color: var(--muted);
  }
  .contact-name {
    font-size: 22px;
    color: var(--orange);
    line-height: 1.1;
  }
  .contact-abn { font-size: 15px; margin-top: 3px; letter-spacing: 0.5px; }
  .contact-line {
    display: flex;
    align-items: center;
    gap: 8px;
    font-size: 15px;
    margin-top: 5px;
    letter-spacing: 0.5px;
  }
  .contact-line svg { width: 14px; height: 14px; flex: none; }
  .services {
    list-style: none;
    margin-top: 28px;
    font-size: 15px;
    color: var(--ink);
    line-height: 1.4;
  }
  .services .services-lead { margin-bottom: 4px; }
</style>
</head>
<body>
<main class="canvas">
  <section class="card card-front" aria-label="Business card front">
    <div class="front-band"></div>
    <div class="front-square"></div>
    <h1 class="front-name">Ashby Paving Works</h1>
  </section>

  <section class="card card-back" aria-label="Business card back">
    <div class="back-block"></div>
    <div class="back-details">
      <p class="contact-name">mark lowry</p>
      <p class="contact-abn">ABN 27613048852</p>
      <p class="contact-line">
        <svg viewBox="0 0 14 14" aria-hidden="true"><rect width="14" height="14" rx="2" fill="#ee6a1f"/><path d="M4 3.5c0 4 2.5 6.5 6.5 7l1-1.8-2-1-1 1c-1.2-.6-2-1.4-2.6-2.6l1-1-1-2z" fill="#fff"/></svg>
        0412885107
      </p>
      <p class="contact-line">
        <svg viewBox="0 0 14 14" aria-hidden="true"><rect y="2" width="14" height="10" rx="1.5" fill="#ee6a1f"/><path d="M1.5 3.5 7 8l5.5-4.5" fill="none" stroke="#fff" stroke-width="1.3"/></svg>
        marklowry@pavemail.com.au
      </p>
      <ul class="services">
        <li class="services-lead">For all your concreting solutions</li>
        <li>Excavation</li>
        <li>Exposed &amp; colour concrete</li>
        <li>House &amp; shed slabs</li>
        <li>Driveways</li>
        <li>Landing &amp; steps</li>
      </ul>
    </div>
  </section>
</main>
</body>
</html>
```